Design einer Kundenbroschüre für Onlineplattform
Zielgruppe
Wir sind eine Onlineplattform, die den Einstieg in die Elektromobilität für Neuwagenkunden so einfach wie das Buchen einer Pauschalreise macht. Unser Kunden erhalten dafür ein individuell auf ihre Bedürfnisse abgestimmstes Gesamtpaket aus E-Auto, Ladelösung, Ökostrom und mehr.
In diesem Wettbewerb wollen wir von Euch eine Kundenbroschüre entwerfen lassen, die Kunden von Autohäusern zur Verfügung gestellt werden soll. Dabei steht im Vordergrund, dass der Prozess bzw. unsere Leistung einfach und verständlich ist.
Hintergrundwissen:
Im Gegensatz zu herkömmlichen Autokauf ist bei einem Kauf eines Elektroauto deutlich mehr zu beachten. So müssen nebem dem Auto noch weitere Komponenten beachtet werden. Im Detail handelt es sich dabei um fünf zusätzliche Komponenten:
1. Laden zu Hause: Eine geeignete Ladelösung zum Laden des E-Autos zu Hause zu finden und diese installieren lassen
2. Laden unterwegs: Eine passende Ladekarte für das Laden unterwegs (In- und Ausland) raussuchen.
3. Ökostrom/Autostrom: Einen günstigen und ökologischen Stromtarif finden
4. Digital Services & Apps: Anwendungen, die die Elektromobilität im Alltag vereinfachen
5. Umweltbonus : Unterstützung bei der Suche und Beantragung der Förderprämie (Umweltbonus) für Elektroautos
Wir übernehmen diese fünf Komponenten für die Kunden eines Autohauses und möchten diese im Vorfeld mit der Broschüre über unseren Service informieren.
Die Kunden sind dabei zwischen 30 und 60 Jahren, Neuwagenkäufer einer Premiummarke und beschäftigen sich mit dem Thema Elektromobilität vermutlich zum ersten Mal.
Aufgabenstellung
Es sollten folgende Themenfelder berücksichtigt sein:
1. Cover mit Logo und Bild ggf. weiteres Element
2. Über uns
3. Eine Übersicht wie der Prozess abläuft (Customer Journey).
4. Eine separate Übersicht über unsere Leistungen im allgemeinen
5. Eine separate Übersicht über unser spezielles Produkt.
Wir haben Euch im Anhang unseren ersten Entwurf angehängt. An diesen müsst ihr euch in keiner Weise halten, allerdings sollten sich die Texte auf den entsprechenden Seiten wiederfinden
Auf jeder Seite sollte in der Fußzeile unser Impressum (als Platzhalter einfügen bitte)
Bitte ausdrücklich nicht das Design unsere momentanen Website als Maßstab nehmen!
Schriftart: Open Sans
Farbcodes:
rosa/pink (HEX: #FF0083, RGB: (255,0,131), CMYK: (0, 100, 49,0))
grau: irgendeine RGBA Abstufung von Schwarz oder #4A4A4A

```html
<!DOCTYPE html>
<html lang="de">
<head>
<meta charset="utf-8">
<title>Leicht Elektrisch – Kundenbroschüre</title>
<link rel="stylesheet" href="https://fonts.googleapis.com/css2?family=Open+Sans:wght@400;600;700;800&display=swap">
<style>
  :root{
    --frame:#4b4697;
    --purple:#4a3f98;
    --pink:#e5338a;
    --text:#2b2b2b;
    --grey:#4a4a4a;
    --label:#dcdcdc;
    --stage:#ffffff;
  }
  *{box-sizing:border-box;margin:0;padding:0}
  html,body{width:778px;height:1200px;overflow:hidden;background:var(--stage)}
  body{position:relative;font-family:"Open Sans",Arial,sans-serif;color:var(--text)}
  .page{position:absolute;width:333px;height:471px;background:var(--frame);box-shadow:0 2px 8px rgba(0,0,0,.12)}
  .sheet{position:absolute;left:12px;top:12px;right:12px;bottom:12px;background:#fff}
  .abs{position:absolute}
  .page-label{position:absolute;width:333px;text-align:center;font-weight:800;font-size:25px;letter-spacing:1px;color:var(--label)}

  /* cover */
  .cover-ring{left:42px;top:67px;width:252px;height:252px;border-radius:50%;
    background:radial-gradient(circle at 30% 30%,#f07ac0 0%,#d8338f 40%,#6a3fa6 80%,#3f3a8c 100%)}
  .cover-core{left:83px;top:106px;width:172px;height:172px;border-radius:50%;background:#fff;
    display:flex;align-items:center;justify-content:center;flex-direction:column;gap:6px}
  .cover-core .mark{width:26px;height:26px;border-radius:50%;background:var(--pink)}
  .cover-core .name{font-weight:800;font-size:17px;color:var(--purple)}
  .cover-banner{left:51px;top:268px;width:232px;height:75px;background:var(--pink);border-radius:6px;
    color:#fff;text-align:center}
  .cover-banner h1{font-size:23px;font-weight:700;line-height:1;margin-top:18px}
  .cover-banner p{font-size:12.5px;margin-top:7px}
  .cover-skyline{left:12px;top:404px;width:309px;height:55px;
    background:linear-gradient(180deg,#fff 0%,#f1f1f4 60%,#e4e4ea 100%)}

  /* headers */
  .head-title{font-size:11.5px;font-weight:700;color:var(--purple);line-height:1.1}
  .head-sub{font-size:8.6px;color:var(--pink);line-height:1.3}
  .brand{display:flex;flex-direction:column;align-items:center;gap:2px}
  .brand .dot{width:14px;height:14px;background:var(--pink);border-radius:50%}
  .brand span{font-size:3.6px;font-weight:700;color:var(--purple)}

  .card{background:#fff;border-radius:5px;box-shadow:0 0 4px rgba(0,0,0,.16)}
  .card h3{font-size:6.6px;font-weight:700;color:var(--purple);margin-bottom:4px}
  .card p{font-size:5.1px;line-height:7.8px;color:var(--text)}
  .card b{font-weight:700}

  .photo{left:30px;top:202px;width:273px;height:95px;border-radius:6px 6px 0 0;
    background:radial-gradient(circle at 38% 50%,#e83f98 0%,#6b2a5c 14%,#2b2b2f 28%,#3c3c42 60%,#1f1f23 100%)}

  .contact-q{left:24px;top:432px}
  .contact{font-size:6.8px;color:var(--pink);display:flex;align-items:center;gap:4px}

  .footer{font-size:4px;line-height:5.6px;color:var(--text)}
  .footer b{font-weight:700}
  .partners{display:flex;align-items:center;gap:6px}
  .partners .badge{width:11px;height:11px;border-radius:50%;background:#3a3a3a}
  .partners span{font-size:5.4px;font-weight:800;line-height:5.6px;color:var(--text)}

  /* services */
  .svc-icon{width:50px;height:50px;border-radius:50%;background:var(--pink);display:flex;align-items:center;justify-content:center}
  .svc-card{width:248px;height:53px;padding:8px 14px 0 26px}
  .svc-card h3{font-size:6.6px}
  .svc-card p{font-size:5px;line-height:7.7px}

  /* journey */
  .node{width:54px;height:54px;border-radius:50%;background:var(--pink);display:flex;align-items:center;justify-content:center;box-shadow:0 0 4px rgba(0,0,0,.2)}
  .node.you{background:#fff;flex-direction:column;gap:1px}
  .node.you span{font-size:5px;font-weight:700}
  .node.final{background:var(--purple);color:#fff;font-size:6.8px;font-weight:600;text-align:center;line-height:9px;border:3px solid #fff}
  .step{padding:8px 5px 0;text-align:center}
  .step h3{font-size:6.6px;margin-bottom:4px}
  .step p{font-size:5.2px;line-height:7.8px}
</style>
</head>
<body>

<!-- Seite 1: Cover -->
<section class="page" style="left:41px;top:45px">
  <div class="sheet"></div>
  <div class="abs cover-ring" role="img" aria-label="Ring aus pink-violetten Blitzen"></div>
  <div class="abs cover-core">
    <div class="mark"></div>
    <div class="name">Leicht Elektrisch</div>
  </div>
  <div class="abs cover-banner">
    <h1>Leicht Elektrisch</h1>
    <p>Ihr Partner für die E-Mobilität</p>
  </div>
  <div class="abs cover-skyline" role="img" aria-label="Strichzeichnung einer Stadtsilhouette mit Bergen, Windrädern und E-Autos"></div>
</section>
<div class="page-label" style="left:41px;top:540px">SEITE 1</div>

<!-- Seite 2: Über uns -->
<section class="page" style="left:405px;top:45px">
  <div class="sheet"></div>
  <div class="abs" style="left:24px;top:31px">
    <div class="head-title">Leicht Elektrisch</div>
    <div class="head-sub">Ihr Partner für E-Mobilität</div>
  </div>
  <div class="abs brand" style="left:280px;top:28px"><div class="dot"></div><span>Leicht Elektrisch</span></div>

  <div class="abs card" style="left:24px;top:70px;width:138px;height:121px;padding:6px 6px">
    <h3>Über uns</h3>
    <p><b>Leicht Elektrisch</b> ist ein führender E-Mobilitätsberater aus Oberbayern, der Ihnen den Einstieg in die Elektromobilität erleichtert. Wir bieten unseren Kunden ein individuell auf Ihre Bedürfnisse abgestimmtes <b>Gesamtpaket aus E-Auto, Ladelösung, Ökostrom und mehr.</b> Sie können den Service ganz einfach von Zuhause nutzen und bekommen alle nötigen Informationen online zugesendet. Zudem haben Sie immer die Möglichkeit, sich <b>kostenfrei</b> telefonisch bei unserem Kundenservice zu melden.</p>
  </div>
  <div class="abs card" style="left:172px;top:70px;width:138px;height:121px;padding:6px 6px">
    <h3>Wer wir sind</h3>
    <p><b>Leicht Elektrisch</b> ist ein Team aus leidenschaftlichen langjährigen E-Mobilitätsexperten, Ladelösungsspezialisten, Stromnetzverstehern, Finanzexperten, sowie Steuer- und Rechtswissenschaftlern, die sich für die Zukunft unserer Mobilität begeistern! Unser Ziel ist es, den Einstieg in die Elektromobilität <b>einfach, kundenorientiert und zeitsparend</b> zu gestalten. Wir helfen Ihnen, das richtige Gesamtpaket zu finden und kümmern uns auch um Details wie Terminvereinbarungen &amp; Koordination von Handwerkern.</p>
  </div>

  <div class="abs photo" role="img" aria-label="Nahaufnahme eines leuchtenden Startknopfs mit der Aufschrift E-Mobility Start"></div>

  <div class="abs card" style="left:24px;top:297px;width:286px;height:80px;padding:6px 6px;display:grid;grid-template-columns:1fr 1fr;column-gap:12px">
    <div>
      <h3>Wie funktioniert´s</h3>
      <p>Ihr persönlicher Kundenberater des <b>Autohauses Brandl + Seidl</b> hat Ihnen einen personalisierten Link zur Verfügung gestellt, der zu unserem Online-Assistenten führt. Sie starten den Assistenten und beantworten ein paar Fragen. Unser Team analysiert auf Basis Ihrer Antworten Ihre individuellen</p>
    </div>
    <div style="padding-top:12px">
      <p>Bedürfnisse und bespricht mit Ihnen die Details des <b>rund-um-sorglos Gesamtpakets.</b> Im Anschluss kümmert sich das Team von Leicht Elektrisch um die Organisation &amp; Koordination des gesamten weiteren Prozesses inkl. Handwerkerterminen und steht Ihnen jederzeit beratend zur Seite.</p>
    </div>
  </div>

  <div class="abs" style="left:24px;top:388px">
    <div class="head-title" style="font-size:9.2px">Sie haben Fragen zum Thema E-Mobilität?</div>
    <div style="display:flex;gap:16px;margin-top:3px">
      <div class="contact">
        <svg width="9" height="9" viewBox="0 0 24 24" fill="none" stroke="#555" stroke-width="1.6"><path d="M5 3h4l2 5-3 2a11 11 0 0 0 6 6l2-3 5 2v4a2 2 0 0 1-2 2A18 18 0 0 1 3 5a2 2 0 0 1 2-2z"/></svg>
        +49 89 40 12 88 50
      </div>
      <div class="contact">
        <svg width="10" height="8" viewBox="0 0 24 18" fill="none" stroke="#555" stroke-width="1.6"><rect x="1" y="1" width="22" height="16"/><path d="M1 1l11 9 11-9"/></svg>
        service@leicht-elektrisch.de
      </div>
    </div>
  </div>

  <div class="abs footer" style="left:24px;top:425px">
    <b>Leicht Elektrisch Mobility GmbH</b><br>Sitz der Gesellschaft: Gauting, Deutschland<br>Registergericht: AG München, HRB 501277<br>Geschäftsführer: Jonas Rieder, Paul Hartl, Lena Amsel
  </div>
  <div class="abs partners" style="left:230px;top:437px"><div class="badge"></div><div class="badge"></div><span>Brandl +<br>Seidl</span></div>
</section>
<div class="page-label" style="left:405px;top:540px">SEITE 2</div>

<!-- Seite 3: Serviceangebot -->
<section class="page" style="left:42px;top:625px">
  <div class="sheet"></div>
  <div class="abs" style="left:24px;top:31px">
    <div class="head-title">Unser Serviceangebot</div>
    <div class="head-sub">Alles für den sorgenfreien Einstieg in die Elektromobilität</div>
  </div>
  <div class="abs brand" style="left:280px;top:28px"><div class="dot"></div><span>Leicht Elektrisch</span></div>

  <div class="abs card svc-card" style="left:62px;top:86px">
    <h3>Wallbox – Zuhause laden</h3>
    <p>Wir evaluieren, ob für Sie zuhause eine Wallbox infrage kommt oder ob Sie auf öffentliche Lademöglichkeiten zugreifen können. Ferner organisieren wir die Standortanalyse Vorort sowie den Einbau und Anschluss der Wallbox.</p>
  </div>
  <div class="abs svc-icon" style="left:24px;top:88px">
    <svg width="30" height="30" viewBox="0 0 24 24" fill="none" stroke="#fff" stroke-width="1"><path d="M6 3h9l2 3v10l-6 5-5-5z"/><path d="M8 4v11"/><path d="M17 9h2v5h-2"/></svg>
  </div>

  <div class="abs card svc-card" style="left:62px;top:150px;height:55px">
    <h3>Auto- &amp; Ökostrom</h3>
    <p>Wir analysieren für Sie, ob Sie mit einem Auto- oder Ökostromtarif noch günstiger Elektroauto fahren können und unterstützen Sie hier beim Stromanbieter- oder Tarifwechsel. Auch beim Thema Solarstrom stehen wir unterstützend zur Seite.</p>
  </div>
  <div class="abs svc-icon" style="left:24px;top:153px">
    <svg width="30" height="30" viewBox="0 0 24 24" fill="none" stroke="#fff" stroke-width="1"><path d="M9 15a5 5 0 1 1 5 0v2H9z"/><path d="M9 19h5M10 21h3M12 2v2M4 9H2M21 9h-2M5 4l1.5 1.5M18 4l-1.5 1.5"/><path d="M16 20c0-3 2-5 6-5-0 3-2 5-6 5z" fill="#fff"/></svg>
  </div>

  <div class="abs card svc-card" style="left:62px;top:216px">
    <h3>Ladekarten – Laden unterwegs</h3>
    <p>Damit Sie auch unterwegs und im Ausland an öffentlichen Ladesäulen Ihr E-Auto überall laden können, finden wir abgestimmt auf die jeweiligen Nutzungsverhalten und Bedürfnisse die passenden Ladekarten.</p>
  </div>
  <div class="abs svc-icon" style="left:24px;top:218px">
    <svg width="30" height="30" viewBox="0 0 24 24" fill="none" stroke="#fff" stroke-width="1"><rect x="4" y="3" width="7" height="16"/><path d="M3 21h9M8 8l-2 4h3l-2 4"/><path d="M15 6v3M19 6v3M14 9h6v3a3 3 0 0 1-6 0zM17 15v4h3"/></svg>
  </div>

  <div class="abs card svc-card" style="left:62px;top:281px">
    <h3>Digital Services &amp; Apps</h3>
    <p>Zusätzlich schnüren wir für unsere Kunden ein Paket aus nützlichen Apps zum Thema Elektromobilität, die Ihnen den Alltag mit Ihrem neuen Elektroauto erleichtern.</p>
  </div>
  <div class="abs svc-icon" style="left:24px;top:283px">
    <svg width="30" height="30" viewBox="0 0 24 24" fill="none" stroke="#fff" stroke-width="1"><rect x="2" y="4" width="20" height="13" rx="1"/><path d="M2 14h20M12 17v3M8 20h8"/><circle cx="12" cy="9.5" r="2"/></svg>
  </div>

  <div class="abs card svc-card" style="left:62px;top:345px">
    <h3>Umweltbonus</h3>
    <p>Wir unterstützen Sie bei der Beantragung des staatlichen Umweltbonus und tragen dafür Sorge, das Sie alle für den Antrag notwendigen Unterlagen rechtzeitig vorliegen haben.</p>
  </div>
  <div class="abs svc-icon" style="left:24px;top:347px">
    <svg width="30" height="30" viewBox="0 0 24 24" fill="none" stroke="#fff" stroke-width="1"><rect x="4" y="3" width="13" height="18"/><path d="M7 8h7M7 11h7M7 14h4M19 6l-8 10-1 3 3-1 8-10z"/></svg>
  </div>

  <div class="abs footer" style="left:24px;top:425px">
    <b>Leicht Elektrisch Mobility GmbH</b><br>Sitz der Gesellschaft: Gauting, Deutschland<br>Registergericht: AG München, HRB 501277<br>Geschäftsführer: Jonas Rieder, Paul Hartl, Lena Amsel
  </div>
  <div class="abs partners" style="left:230px;top:437px"><div class="badge"></div><div class="badge"></div><span>Brandl +<br>Seidl</span></div>
</section>
<div class="page-label" style="left:42px;top:1123px">SEITE 3</div>

<!-- Seite 4: Customer Journey -->
<section class="page" style="left:405px;top:625px">
  <div class="sheet"></div>
  <div class="abs" style="left:24px;top:31px">
    <div class="head-title">Und so geht es weiter</div>
    <div class="head-sub">Der Weg von E-Auto bis Umweltbonus</div>
  </div>
  <div class="abs brand" style="left:280px;top:28px"><div class="dot"></div><span>Leicht Elektrisch</span></div>

  <svg class="abs" style="left:0;top:0" width="333" height="471" viewBox="0 0 333 471">
    <path d="M77 95H288a20 20 0 0 1 20 20v80a20 20 0 0 1-20 20H44a20 20 0 0 0-20 20v80a20 20 0 0 0 20 20H256" fill="none" stroke="#4a3f98" stroke-width="5"/>
    <g fill="#e5338a">
      <path d="M119 89l7 6-7 6z"/><path d="M209 89l7 6-7 6z"/>
      <path d="M302 148h12l-6 7z"/>
      <path d="M171 209l-7 6 7 6z"/>
      <path d="M18 272h12l-6 7z"/>
      <path d="M119 329l7 6-7 6z"/><path d="M209 329l7 6-7 6z"/>
    </g>
  </svg>

  <div class="abs node you" style="left:50px;top:68px">
    <svg width="20" height="18" viewBox="0 0 24 20" fill="none" stroke="#333" stroke-width="1"><circle cx="6" cy="3" r="2"/><circle cx="12" cy="3" r="2"/><circle cx="18" cy="3" r="2"/><path d="M3 18V8h6v10M9 18V8h6v10M15 18V8h6v10"/></svg>
    <span>Sie</span>
  </div>
  <div class="abs node" style="left:139px;top:68px">
    <svg width="28" height="28" viewBox="0 0 24 24" fill="none" stroke="#fff" stroke-width="1.2"><circle cx="10" cy="10" r="6"/><path d="M14.5 14.5L21 21"/></svg>
  </div>
  <div class="abs node" style="left:229px;top:68px">
    <svg width="28" height="28" viewBox="0 0 24 24" fill="none" stroke="#fff" stroke-width="1"><path d="M6 3h9l2 3v10l-6 5-5-5z"/><path d="M8 4v11"/><path d="M17 9h2v5h-2"/></svg>
  </div>
  <div class="abs card step" style="left:130px;top:116px;width:74px;height:56px">
    <h3>1. Bedarfsanalyse</h3>
    <p>Beratung &amp; Zusammenstellung des passenden Gesamtpakets.</p>
  </div>
  <div class="abs card step" style="left:219px;top:116px;width:74px;height:67px">
    <h3>2. Ladelösung</h3>
    <p>Beratung zur Ladelösung, Vereinbarung einer Standortanalyse &amp; Koordination des Einbaus der Wallbox.</p>
  </div>

  <div class="abs node" style="left:199px;top:188px">
    <svg width="28" height="28" viewBox="0 0 24 24" fill="none" stroke="#fff" stroke-width="1"><rect x="4" y="3" width="7" height="16"/><path d="M3 21h9M8 8l-2 4h3l-2 4"/><path d="M15 6v3M19 6v3M14 9h6v3a3 3 0 0 1-6 0zM17 15v4h3"/></svg>
  </div>
  <div class="abs node" style="left:78px;top:188px">
    <svg width="28" height="28" viewBox="0 0 24 24" fill="none" stroke="#fff" stroke-width="1"><path d="M9 15a5 5 0 1 1 5 0v2H9z"/><path d="M9 19h5M10 21h3M12 2v2M4 9H2M21 9h-2"/><path d="M16 20c0-3 2-5 6-5 0 3-2 5-6 5z" fill="#fff"/></svg>
  </div>
  <div class="abs card step" style="left:181px;top:237px;width:87px;height:54px">
    <h3>3. Laden unterwegs</h3>
    <p>Ermittlung bedarfsgerechter Ladekarten für öffentliche Ladesäulen.</p>
  </div>
  <div class="abs card step" style="left:64px;top:237px;width:90px;height:64px">
    <h3>4. Auto- &amp; Ökostrom</h3>
    <p>Ermittlung passender Autostromtarife zum nachhaltigen Laden des E-Autos zu Hause.</p>
  </div>

  <div class="abs node" style="left:50px;top:308px">
    <svg width="28" height="28" viewBox="0 0 24 24" fill="none" stroke="#fff" stroke-width="1"><rect x="2" y="4" width="20" height="13" rx="1"/><path d="M2 14h20M12 17v3M8 20h8"/><circle cx="12" cy="9.5" r="2"/></svg>
  </div>
  <div class="abs node" style="left:139px;top:308px">
    <svg width="28" height="28" viewBox="0 0 24 24" fill="none" stroke="#fff" stroke-width="1"><rect x="4" y="3" width="13" height="18"/><path d="M7 8h7M7 11h7M7 14h4M19 6l-8 10-1 3 3-1 8-10z"/></svg>
  </div>
  <div class="abs node final" style="left:229px;top:308px">Übergabe<br>E-Auto</div>
  <div class="abs card step" style="left:35px;top:357px;width:84px;height:47px">
    <h3>5. Digital Services</h3>
    <p>Beratung zu digitalen Services, die die E-Mobilität im Alltag vereinfachen.</p>
  </div>
  <div class="abs card step" style="left:129px;top:357px;width:75px;height:47px">
    <h3>6. Umweltbonus</h3>
    <p>Unterstützung bei Beantragung des staatlichen Umweltbonus.</p>
  </div>

  <div class="abs footer" style="left:24px;top:425px">
    <b>Leicht Elektrisch Mobility GmbH</b><br>Sitz der Gesellschaft: Gauting, Deutschland<br>Registergericht: AG München, HRB 501277<br>Geschäftsführer: Jonas Rieder, Paul Hartl, Lena Amsel
  </div>
  <div class="abs partners" style="left:230px;top:437px"><div class="badge"></div><div class="badge"></div><span>Brandl +<br>Seidl</span></div>
</section>
<div class="page-label" style="left:405px;top:1123px">SEITE 4</div>

</body>
</html>
```